to-go container produts catalogue

we sell different kinds of to-go containers and need to make a catalogue for our cosumers.
Most of them are restraunts owner and some of them are distrunutors.
Our company named "Bright Meadow Packaging"
Our website is www.brightmeadowpackaging.com
our produts are quite like we showed on web.
We also have other produtcs need to be showed in the catalogue
We have different product lines and each type have different size.
We hope the catalogue is simple and clear. maybe a little industrial style

```html
<!DOCTYPE html>
<html lang="en">
<head>
<meta charset="utf-8">
<title>Bright Meadow Packaging – Product Catalogue</title>
<link href="https://fonts.googleapis.com/css2?family=Oswald:wght@300;400;600;700&family=Poppins:wght@300;400;500;600&display=swap" rel="stylesheet">
<style>
:root{
  --green:#3fc497;
  --green-dark:#2fae83;
  --navy:#1c3a6e;
  --navy-deep:#15305d;
  --blue:#2a6db5;
  --blue-soft:#dce8f4;
  --paper:#ffffff;
  --paper-grey:#eef0f1;
  --ink:#4a4f57;
  --stage:#8a8c8b;
}
*{box-sizing:border-box;margin:0;padding:0}
html,body{width:858px;height:1200px;overflow:hidden;background:var(--stage)}
body{position:relative;font-family:"Poppins",sans-serif;color:var(--ink)}
.spread{position:absolute;left:29px;width:800px;height:560px;display:flex;box-shadow:0 6px 18px rgba(0,0,0,.25)}
.spread--cover{top:24px}
.spread--inner{top:616px}
.page{position:relative;width:400px;height:560px;background:var(--paper);overflow:hidden}
.photo{position:absolute}

/* back cover */
.back-cover{background:linear-gradient(180deg,#f7f8f8,var(--paper-grey))}
.back-cover .green-field{position:absolute;inset:0}
.feature-row{position:absolute;top:95px;left:0;width:100%;display:flex;justify-content:space-around;padding:0 20px}
.feature{width:100px;text-align:center;color:var(--blue);font-size:10px;font-weight:600;line-height:1.2}
.feature .badge{width:58px;height:58px;margin:0 auto 8px;border-radius:50%;border:3px solid var(--navy);background:#f3f5f8}
.feature .ship-art{width:78px;height:42px;margin:8px auto 16px;border-radius:6px;background:linear-gradient(90deg,#9aa4ae,var(--blue))}
.feature .print-art{width:50px;height:50px;margin:4px auto 12px;border-radius:6px;background:linear-gradient(160deg,#6fb5e5,var(--navy))}
.contact-list{position:absolute;top:330px;left:0;width:100%;text-align:center;color:#fff;font-size:11.5px;font-weight:500;list-style:none}
.contact-list li{margin-bottom:16px;display:flex;flex-direction:column;align-items:center;gap:5px}
.contact-list svg{width:16px;height:16px}

/* front cover */
.front-cover .green-field{position:absolute;inset:0}
.cover-header{position:absolute;top:22px;left:18px;right:14px;height:66px;background:#fff;display:flex;align-items:center;padding:0 12px;gap:12px}
.brand{display:flex;align-items:center;gap:6px;font-family:"Oswald",sans-serif;font-weight:600;font-size:15px;line-height:1.05;color:var(--blue);width:118px}
.brand .mark{width:12px;height:12px;background:var(--green);flex:none}
.cover-title{border-left:2px solid var(--blue);padding-left:10px}
.cover-title h1{font-family:"Oswald",sans-serif;font-weight:700;font-size:22px;color:var(--blue);letter-spacing:.2px;line-height:1.1}
.cover-title p{font-size:9.5px;font-weight:500;color:var(--green-dark)}
.front-cover .hero{left:44px;top:100px;width:356px;height:270px;background:linear-gradient(135deg,#c9c3b8 0%,#8e8a85 45%,#2e2c2b 100%)}
.category-strip{position:absolute;top:392px;left:22px;right:14px;display:flex;justify-content:space-between}
.category{width:56px;text-align:center;font-size:6.5px;line-height:1.25;color:var(--blue)}
.category .thumb{height:44px;border:2px solid var(--blue-soft);background:linear-gradient(160deg,#eef1f4,#9aa3ad);margin-bottom:5px}
.cover-url{position:absolute;bottom:34px;right:22px;font-size:9px;font-weight:600;letter-spacing:1.5px;color:var(--green-dark)}

/* inner pages */
.section-photo{left:22px;top:22px;width:210px;height:170px;background:linear-gradient(135deg,#d7d2c4,#9c9f7a 55%,#3a3a38)}
.blue-accent{position:absolute;left:22px;top:12px;width:70px;height:10px;background:var(--blue)}
.section-panel{position:absolute;left:232px;top:0;width:168px;height:192px;background:linear-gradient(160deg,var(--blue),var(--navy-deep))}
.section-frame{position:absolute;left:14px;top:30px;width:140px;height:118px;border-top:3px solid #fff;border-right:3px solid #fff}
.section-frame::after{content:"";position:absolute;left:-4px;bottom:-14px;width:110px;height:60px;border-left:3px solid #fff;border-bottom:3px solid #fff}
.section-title{position:absolute;left:22px;top:40px;width:130px;text-align:center;font-family:"Oswald",sans-serif;color:#fff;font-size:19px;font-weight:300;line-height:1.3}
.section-title strong{font-weight:600}
.product-grid{position:absolute;display:grid;grid-template-columns:repeat(3,1fr);grid-template-rows:repeat(3,1fr)}
.micro-grid{left:22px;right:0;top:200px;height:316px;background:linear-gradient(180deg,#fafbfc,#f1f3f5)}
.micro-grid .product{border-right:1px solid #e3e7eb;border-bottom:1px solid #e3e7eb;display:flex;flex-direction:column;align-items:center;justify-content:space-between;padding:10px 6px 8px}
.product .shot{width:64px;height:34px;border-radius:8px;background:linear-gradient(160deg,#8b9096,#1f2226);margin-top:6px}
.micro-grid .label{background:var(--blue-soft);font-size:7px;font-weight:300;text-align:center;line-height:1.3;padding:5px 6px;width:100%}
.footer-line{position:absolute;bottom:14px;font-size:7.5px;letter-spacing:3px;color:var(--green)}
.footer-bar{position:absolute;left:0;bottom:0;width:130px;height:8px;background:var(--blue)}

.clamshell-head{position:absolute;left:0;top:0;width:200px;height:170px;background:#fff}
.clamshell-frame{position:absolute;left:20px;top:40px;width:140px;height:82px;border-top:3px solid var(--navy);border-right:3px solid var(--navy)}
.clamshell-frame::after{content:"";position:absolute;left:-4px;bottom:-8px;width:110px;height:48px;border-left:3px solid var(--blue);border-bottom:3px solid var(--blue)}
.clamshell-title{position:absolute;left:34px;top:52px;width:110px;text-align:center;font-family:"Oswald",sans-serif;font-size:18px;font-weight:400;color:var(--blue);line-height:1.3}
.clamshell-title strong{font-weight:600}
.clamshell-photo{left:200px;top:0;width:200px;height:170px;background:linear-gradient(150deg,#b7bdc3,#6f7780)}
.clam-grid{left:0;right:0;top:170px;height:350px;background:linear-gradient(180deg,var(--navy),var(--navy-deep))}
.clam-grid .product{border-right:1px solid rgba(255,255,255,.12);border-bottom:1px solid rgba(255,255,255,.12);display:flex;flex-direction:column;align-items:center;justify-content:space-between;padding:12px 8px 10px}
.clam-grid .shot{width:42px;height:40px;border-radius:8px;background:linear-gradient(160deg,#ffffff,#d9dde2);margin-top:2px}
.clam-grid .label{background:#fff;font-size:7px;font-weight:300;text-align:center;line-height:1.3;padding:6px 4px;width:100%;color:#333}
.clam-footer{position:absolute;left:0;bottom:0;width:100%;height:40px}
.clam-footer .footer-line{right:14px;bottom:14px}
</style>
</head>
<body>

<section class="spread spread--cover">
  <article class="page back-cover">
    <svg class="green-field" viewBox="0 0 400 560" aria-hidden="true"><polygon points="0,300 400,220 400,560 0,560" fill="var(--green)"/></svg>
    <div class="feature-row">
      <div class="feature"><div class="badge" role="img" aria-label="Business certification badge"></div>Women Owned<br>Business</div>
      <div class="feature"><div class="ship-art" role="img" aria-label="Delivery truck over a country map"></div>Nationwide<br>Delivery</div>
      <div class="feature"><div class="print-art" role="img" aria-label="Printer illustration"></div>Custom<br>Printing</div>
    </div>
    <ul class="contact-list">
      <li><svg viewBox="0 0 24 24"><path d="M12 2a7 7 0 0 0-7 7c0 5 7 13 7 13s7-8 7-13a7 7 0 0 0-7-7zm0 9.5A2.5 2.5 0 1 1 12 6.5a2.5 2.5 0 0 1 0 5z" fill="#fff"/></svg>1250 Orchard Ave. Fairview, CA 90210</li>
      <li><svg viewBox="0 0 24 24"><path d="M6.6 10.8a15 15 0 0 0 6.6 6.6l2.2-2.2a1 1 0 0 1 1-.25 11.4 11.4 0 0 0 3.6.57 1 1 0 0 1 1 1V20a1 1 0 0 1-1 1A17 17 0 0 1 3 4a1 1 0 0 1 1-1h3.5a1 1 0 0 1 1 1c0 1.25.2 2.45.57 3.57a1 1 0 0 1-.25 1z" fill="#fff"/></svg>555-014-2200</li>
      <li><svg viewBox="0 0 24 24"><path d="M3 5h18v14H3z M3 5l9 8 9-8" fill="none" stroke="#fff" stroke-width="2"/></svg>cs@brightmeadowpackaging.com</li>
      <li><svg viewBox="0 0 24 24"><circle cx="12" cy="12" r="9" fill="none" stroke="#fff" stroke-width="2"/><path d="M3 12h18M12 3c3 3 3 15 0 18M12 3c-3 3-3 15 0 18" fill="none" stroke="#fff" stroke-width="1.6"/></svg>www.brightmeadowpackaging.com</li>
    </ul>
  </article>

  <article class="page front-cover">
    <svg class="green-field" viewBox="0 0 400 560" aria-hidden="true"><polygon points="0,0 400,0 400,60 44,330 0,330" fill="var(--green)"/></svg>
    <header class="cover-header">
      <div class="brand"><span class="mark"></span><span>Bright Meadow Packaging</span></div>
      <div class="cover-title">
        <h1>RESTAURANTS BEST CHOICE!</h1>
        <p>Eco-Friendly. Sustainable. Wholesale Prices</p>
      </div>
    </header>
    <div class="photo hero" role="img" aria-label="Kitchen counter with black take-out containers being filled with salad"></div>
    <div class="category-strip">
      <div class="category"><div class="thumb" role="img" aria-label="Stacked microwaveable containers"></div>Microwaveable Take-Out Containers</div>
      <div class="category"><div class="thumb" role="img" aria-label="Stacked clamshell containers"></div>Clamshell Contaier</div>
      <div class="category"><div class="thumb" role="img" aria-label="Paper cups and boxes"></div>Paper Products</div>
      <div class="category"><div class="thumb" role="img" aria-label="Stacked portion cups"></div>Portion Cups and Lids</div>
      <div class="category"><div class="thumb" role="img" aria-label="Wooden cutlery set"></div>Cutlery/ Utensil</div>
      <div class="category"><div class="thumb" role="img" aria-label="Black sushi trays"></div>Sushi Container</div>
    </div>
    <div class="cover-url">WWW.BRIGHTMEADOWPACKAGING.COM</div>
  </article>
</section>

<section class="spread spread--inner">
  <article class="page micro-page">
    <span class="blue-accent"></span>
    <div class="photo section-photo" role="img" aria-label="Gloved hand closing a lid on a rice and vegetable meal container"></div>
    <div class="section-panel">
      <div class="section-frame"></div>
      <h2 class="section-title"><strong>Microwaveable</strong><br>Take-Out<br>Containers</h2>
    </div>
    <div class="product-grid micro-grid">
      <div class="product"><div class="shot" role="img" aria-label="58oz container"></div><p class="label">58oz Microwaveable Container with Lid 150 Sets</p></div>
      <div class="product"><div class="shot" role="img" aria-label="48oz square container"></div><p class="label">48oz Square Microwaveable Container with Lid 3 Compartment 100 Sets</p></div>
      <div class="product"><div class="shot" role="img" aria-label="39oz container"></div><p class="label">39oz Rectangular Microwaveable Container with Lid 3 Compartment 150 Sets</p></div>
      <div class="product"><div class="shot" role="img" aria-label="38oz container"></div><p class="label">38oz Rectangular Microwaveable Container with Lid 150 Sets</p></div>
      <div class="product"><div class="shot" role="img" aria-label="33oz container"></div><p class="label">33oz Rectangular Microwaveable Container with Lid 3 Compartment 150 Sets</p></div>
      <div class="product"><div class="shot" role="img" aria-label="32oz container"></div><p class="label">32oz Rectangular Microwaveable Container with Lid Compartment 150 Sets</p></div>
      <div class="product"><div class="shot" role="img" aria-label="32oz two compartment container"></div><p class="label">32oz Rectangular Microwaveable Container with Lid 2 Compartment 150 Sets</p></div>
      <div class="product"><div class="shot" role="img" aria-label="28oz container"></div><p class="label">28oz Rectangular Microwaveable Container with Lid Compartment 150 Sets</p></div>
      <div class="product"><div class="shot" role="img" aria-label="24oz container"></div><p class="label">24oz Rectangular Microwaveable Container with Lid 150 Sets</p></div>
    </div>
    <p class="footer-line" style="left:150px">FOR MORE OFFERS VISIT - WWW.WESBSITE URL</p>
    <span class="footer-bar"></span>
  </article>

  <article class="page clamshell-page">
    <div class="clamshell-head">
      <div class="clamshell-frame"></div>
      <h2 class="clamshell-title"><strong>Clamshell</strong><br>Contaier</h2>
    </div>
    <div class="photo clamshell-photo" role="img" aria-label="White fiber clamshell container on a stone table"></div>
    <div class="product-grid clam-grid">
      <div class="product"><div class="shot" role="img" aria-label="3 compartment clamshell"></div><p class="label">Clamshell Contaier 3 Compartment, Center Slide, 9.5" x 9.25"</p></div>
      <div class="product"><div class="shot" role="img" aria-label="3 compartment clamshell"></div><p class="label">Clamshell Contaier 3 Compartment, Center Slide, 9" x 8.2"</p></div>
      <div class="product"><div class="shot" role="img" aria-label="3 compartment clamshell"></div><p class="label">Clamshell Contaier 3 Compartment, Center Slide, 8.25" x 7.55"</p></div>
      <div class="product"><div class="shot" role="img" aria-label="Single clamshell"></div><p class="label">Clamshell Contaier Center Slide, 9.5" x 9.25"</p></div>
      <div class="product"><div class="shot" role="img" aria-label="Single clamshell"></div><p class="label">Clamshell Contaier Center Slide, 9" x 8.2"</p></div>
      <div class="product"><div class="shot" role="img" aria-label="3 compartment clamshell"></div><p class="label">Clamshell Contaier 3 Compartment, Center Slide, 8.25" x 7.55"</p></div>
      <div class="product"><div class="shot" style="width:50px;height:34px" role="img" aria-label="Rectangular clamshell"></div><p class="label">Clamshell Contaier Center Slide, 9.5" x 6.5"</p></div>
      <div class="product"><div class="shot" style="width:50px;height:34px" role="img" aria-label="Rectangular clamshell"></div><p class="label">Clamshell Contaier Center Slide, 8.8" x 5.3"</p></div>
      <div class="product"><div class="shot" style="width:34px" role="img" aria-label="Small clamshell"></div><p class="label">Clamshell Contaier 3 Compartment, Center Slide, 5.25" x 5.25"</p></div>
    </div>
    <div class="clam-footer">
      <svg width="400" height="40" viewBox="0 0 400 40" aria-hidden="true"><polygon points="0,0 120,0 80,40 0,40" fill="var(--navy)"/></svg>
      <p class="footer-line">FOR MORE OFFERS VISIT - WWW.WESBSITE URL</p>
    </div>
  </article>
</section>

</body>
</html>
```